Business Card for Professional Photographer

I'm looking for an eye catching modern clean design that compliments my logo/ website fonts & colours.
I specialise in architecture, corporate & commercial photography so I'm marketing to professional clients rather than portrait / wedding clients.

I would prefer to not have a solid black design.

My logo brand guide is as follows :

Main front font. : Reislust
Main font colour : #fff
Slogan front font : Ubuntu Bold
Monogram front font : Venti Medium
Container colour : #fff

I need print ready files in pdf .png & .eps formats.

Included in the files below are some screen grabs as reference to font & colours etc.

```html
<!DOCTYPE html>
<html lang="en">
<head>
<meta charset="utf-8">
<title>Clearline Studio – Business Card</title>
<link rel="stylesheet" href="https://fonts.googleapis.com/css2?family=Open+Sans:wght@300;400;700&display=swap">
<style>
  :root {
    --page-bg: #55575a;
    --card-bg: #2f3033;
    --card-mark: #3b3c40;
    --gold: #d7ab4a;
    --gold-light: #f3d77e;
    --gold-dark: #b0842c;
    --white: #ffffff;
  }
  * { margin: 0; padding: 0; box-sizing: border-box; }
  html, body {
    width: 1200px; height: 1125px; overflow: hidden;
    background: var(--page-bg);
    font-family: "Open Sans", Arial, sans-serif;
  }
  .canvas { position: relative; width: 1200px; height: 1125px; }

  .card {
    position: absolute; left: 180px; width: 840px; height: 480px;
    background: var(--card-bg); overflow: hidden;
  }
  .card--back { top: 50px; }
  .card--front { top: 595px; }
  .card__edge {
    position: absolute; left: 0; right: 0; bottom: 0; height: 8px;
    background: linear-gradient(90deg, var(--gold-dark), var(--gold-light) 50%, var(--gold));
  }

  /* Back */
  .back-mark {
    position: absolute; left: 0; right: 0; top: 205px;
    text-align: center; color: var(--card-mark);
    font-size: 34px; font-weight: 400; letter-spacing: 8px;
  }

  /* Front */
  .brand { position: absolute; left: 54px; top: 42px; display: flex; align-items: center; gap: 22px; }
  .brand__circle { width: 64px; height: 64px; border: 4px solid var(--gold); border-radius: 50%; }
  .brand__name { color: var(--white); font-size: 28px; font-weight: 300; letter-spacing: 6px; line-height: 1; }
  .brand__tagline { margin-top: 8px; color: var(--gold); font-size: 10px; font-weight: 700; letter-spacing: 2.4px; }

  .person { position: absolute; right: 70px; top: 225px; text-align: right; }
  .person__name {
    font-size: 30px; font-weight: 700; letter-spacing: 1px; line-height: 1.1;
    background: linear-gradient(90deg, var(--gold-dark), var(--gold-light));
    -webkit-background-clip: text; background-clip: text; color: transparent;
  }
  .person__role { color: var(--white); font-size: 20px; font-weight: 400; margin-top: 4px; }

  .divider { position: absolute; left: 70px; right: 70px; top: 312px; height: 1px; background: var(--gold); }

  .contact { position: absolute; left: 60px; top: 330px; list-style: none; }
  .contact__item {
    display: flex; align-items: center; gap: 8px;
    color: var(--white); font-size: 21px; line-height: 30px;
  }
  .contact__icon { width: 17px; height: 17px; fill: var(--gold); flex: none; }
</style>
</head>
<body>
<main class="canvas">

  <section class="card card--back" aria-label="Card back">
    <p class="back-mark">CLEARLINE STUDIO</p>
    <div class="card__edge"></div>
  </section>

  <section class="card card--front" aria-label="Card front">
    <header class="brand">
      <div class="brand__circle"></div>
      <div>
        <p class="brand__name">CLEARLINE STUDIO</p>
        <p class="brand__tagline">Architecture Corporate Commercial</p>
      </div>
    </header>

    <div class="person">
      <p class="person__name">DANIEL HARROW</p>
      <p class="person__role">Director</p>
    </div>

    <div class="divider"></div>

    <ul class="contact">
      <li class="contact__item">
        <svg class="contact__icon" viewBox="0 0 24 24"><path d="M6.6 10.8a15.2 15.2 0 0 0 6.6 6.6l2.2-2.2a1 1 0 0 1 1-.25 11.4 11.4 0 0 0 3.6.57 1 1 0 0 1 1 1V20a1 1 0 0 1-1 1A17 17 0 0 1 3 4a1 1 0 0 1 1-1h3.5a1 1 0 0 1 1 1c0 1.25.2 2.45.57 3.57a1 1 0 0 1-.25 1z"/></svg>
        555 014 2290
      </li>
      <li class="contact__item">
        <svg class="contact__icon" viewBox="0 0 24 24"><path d="M2 5h20v2l-10 6L2 7z"/><path d="M2 9l10 6 10-6v10H2z"/></svg>
        info@clearlinestudio.com
      </li>
      <li class="contact__item">
        <svg class="contact__icon" viewBox="0 0 24 24"><circle cx="12" cy="12" r="10"/><path d="M2 12h20M12 2c3 3 3 17 0 20M12 2c-3 3-3 17 0 20" stroke="#2f3033" stroke-width="1.5" fill="none"/></svg>
        www.clearlinestudio.com
      </li>
    </ul>

    <div class="card__edge"></div>
  </section>

</main>
</body>
</html>
```